Investment website design - investing in mutual funds

I need a design of a website (only homepage for now) dedicated to investment in mutual funds. Attached is a mock up with all the elements the homepage design should contain. The homepage should contain a logo in the upper left corner, the domain the website will run on is www.perovalstrinka.cz , in the upper right corner there should be 2 buttons or links SIGN UP / SIGN IN. The bottom of the homepage should contain links to ABOUT US, FAQ, PRIVACY POLICY, CONTACT US.
Now the main elements on the homepage
1) Video that will explain how the investment works exactly, under this video we will have 3 illustrated icons like the ones attached (see 2nd attachement) that will show the potential investor what exactly they could get when investing with us (education for kids, happy life after they retire, regular monthly payment for the rest of their life).
2) On the right side next to the video we will have a calculator where a potential investor can play with the numbers, the investor can fill in the MONTHLY PAYMENT that he wants to invest regularly every month, the time frame of the investment - for how long he wants to invest. Once the potential investor selects those 2 variables we will calculate for him 2 options - either he can get a ONE TIME PAYOUT once he reaches his investment horizon or he can get a regular monthly payment for the rest of his life. Under the laculator there will be a button 'I want to invest ->'. The functionality of the calculator should be similar to the calculator that can be found here http://www.brodavbank.cz/brodav-podilove-fondy/ and https://felbo.cz/.
The design should look similar to https://felbo.cz/ (font, colors, logo). We prefer white background in the area where we have the video and calculator. We also like the design of www.tarvupo.com. Let me know if you have any questions.

```html
<!DOCTYPE html>
<html lang="en">
<head>
<meta charset="utf-8">
<title>Perovalstrinka – mutual fund investing</title>
<link href="https://fonts.googleapis.com/css2?family=Patrick+Hand&family=PT+Serif:wght@400;700&family=Open+Sans:wght@400&display=swap" rel="stylesheet">
<style>
:root{
  --coral:#e8553a;
  --teal:#45b9c6;
  --teal-dark:#3aa8b5;
  --teal-light:#52c3cf;
  --ice:#dff9fc;
  --ink:#3a3a3a;
  --muted:#8a8a8a;
  --line:#d6d6d6;
  --footer:#4e4c50;
  --footer-dark:#38373a;
  --white:#ffffff;
}
*{box-sizing:border-box;margin:0;padding:0}
html,body{width:702px;height:1200px;overflow:hidden;background:var(--white)}
body{position:relative;font-family:"PT Serif",Georgia,serif;color:var(--ink)}
.abs{position:absolute}

/* header */
.site-header{left:0;top:0;width:702px;height:48px;background:var(--coral)}
.brand{left:50px;top:11px;font-family:"Patrick Hand",cursive;font-size:22px;color:var(--white);letter-spacing:.5px}
.main-nav a{position:absolute;top:18px;font-size:9px;color:var(--white);text-decoration:none;letter-spacing:.3px}
.account-btn{top:14px;height:21px;width:71px;border:1px solid rgba(255,255,255,.8);border-radius:11px;color:var(--white);font-size:9px;display:flex;align-items:center;justify-content:center;text-decoration:none}

/* hero */
.hero{left:0;top:48px;width:702px;height:360px}
.hero-title{left:50px;top:88px;width:300px;font-family:"Patrick Hand",cursive;font-size:30px;line-height:34px;color:var(--white)}
.hero-text{left:50px;top:166px;width:330px;font-size:11.5px;line-height:17px;color:var(--white)}
.hero-btn{top:222px;width:83px;height:31px;background:var(--coral);color:var(--white);font-family:"Patrick Hand",cursive;font-size:13px;display:flex;align-items:center;justify-content:center}
.hero-art{left:382px;top:58px;width:250px;height:262px;border-radius:46% 40% 44% 38%;background:radial-gradient(circle at 55% 55%,#f5a623 0%,#f0a028 45%,#e8553a 90%,rgba(232,85,58,0) 100%)}

/* content */
.section-title{top:436px;font-size:19px;font-weight:400;color:var(--ink);letter-spacing:.2px}
.section-title b{font-weight:400;color:#2c2c2c}
.title-rule{top:466px;width:28px;height:1px;background:var(--coral)}
.video{left:50px;top:483px;width:272px;height:225px;background:linear-gradient(180deg,#d8b62c 0%,#d4b229 72%,#559a3c 76%,#4f9438 100%)}
.video-badge{left:12px;top:12px;width:21px;height:21px;border-radius:50%;background:var(--coral)}

.field{left:358px;width:292px;height:31px;border:1px solid var(--line);font-size:9px;color:var(--muted);padding-left:10px;display:flex;align-items:center;background:var(--white)}
.slider-label{left:370px;top:527px;font-size:9px;color:var(--ink)}
.slider-track{left:365px;top:546px;width:277px;height:3px;background:#e2e2e2}
.slider-fill{left:365px;top:546px;width:114px;height:3px;background:var(--coral)}
.slider-thumb{left:472px;top:540px;width:15px;height:15px;border-radius:50%;background:var(--teal);border:3px solid var(--teal)}
.slider-thumb::after{content:"";position:absolute;left:2px;top:2px;width:5px;height:5px;border-radius:50%;background:var(--white)}
.range-tag{top:559px;height:13px;border:1px solid var(--line);font-size:8px;display:flex;align-items:center;justify-content:center}
.or{left:358px;width:292px;top:615px;text-align:center;font-size:8px}
.invest-btn{left:358px;top:678px;width:292px;height:32px;background:var(--teal);color:var(--white);font-size:11.5px;letter-spacing:.6px;display:flex;align-items:center;justify-content:center}

/* benefits */
.benefit-card{top:808px;width:190px;height:184px;border:1px solid #cfeff3}
.benefit-art{left:44px;top:22px;width:100px;height:98px;border-radius:10px}
.benefit-name{left:0;top:127px;width:100%;text-align:center;font-family:"Patrick Hand",cursive;font-size:15px;line-height:23px;color:#3b3b3b}

/* footer */
.footer-brand{left:0;width:702px;top:1069px;text-align:center;font-family:"Patrick Hand",cursive;font-size:20px;color:var(--white)}
.footer-rule{left:283px;top:1100px;width:114px;height:1px;background:#6a686c}
.footer-nav a{position:absolute;top:1115px;font-size:8.5px;color:var(--white);text-decoration:none}
.footer-sep{top:1115px;font-size:8px;color:#77757a}
.social{top:1141px;width:16px;height:16px;border-radius:50%;background:var(--teal)}
.legal{left:0;top:1178px;width:702px;height:22px;background:var(--footer-dark);font-family:"Open Sans",sans-serif;font-size:7px;color:#77757a;display:flex;align-items:center;justify-content:center}
</style>
</head>
<body>

<header class="site-header abs">
  <div class="brand abs">PEROVALSTRINKA</div>
  <nav class="main-nav">
    <a style="left:210px">ABOUT US</a>
    <a style="left:279px">FAQ</a>
    <a style="left:326px">PRIVACY POLICY</a>
    <a style="left:420px">CONTACT US</a>
  </nav>
  <a class="account-btn abs" style="left:499px">SIGN UP</a>
  <a class="account-btn abs" style="left:580px">SIGN IN</a>
</header>

<section class="hero abs">
  <svg class="abs" style="left:0;top:0" width="702" height="360" viewBox="0 0 702 360">
    <rect width="702" height="360" fill="var(--teal)"/>
    <path d="M0 90 C120 40 300 50 380 130 C420 170 430 260 420 345 L0 320 Z" fill="var(--teal-dark)"/>
    <circle cx="700" cy="40" r="220" fill="var(--teal-light)" opacity=".6"/>
    <polygon points="405,343 430,300 702,280 702,360" fill="var(--coral)"/>
    <polygon points="0,320 702,360 0,360" fill="var(--ice)"/>
  </svg>
  <h1 class="hero-title abs">Lorem Ipsum is simply dummy text</h1>
  <p class="hero-text abs">Lorem Ipsum is simply dummy text of the printing and typesetting industry lorem ipsum.</p>
  <div class="hero-btn abs" style="left:50px">lorem ipsum</div>
  <div class="hero-btn abs" style="left:154px">lorem ipsum</div>
  <div class="hero-art abs" role="img" aria-label="Illustration of a man asleep on a large money-bag beanbag"></div>
</section>

<h2 class="section-title abs" style="left:50px">VIDEO ABOUT OUR <b>PRODUCT</b></h2>
<div class="title-rule abs" style="left:50px"></div>
<h2 class="section-title abs" style="left:359px">OUR ONLINE <b>CALCULATOR</b></h2>
<div class="title-rule abs" style="left:360px"></div>

<div class="video abs" role="img" aria-label="Video still: illustrated figure carrying a big green money sack across a field">
  <div class="video-badge abs">
    <svg width="21" height="21" viewBox="0 0 21 21"><rect x="5" y="7" width="8" height="7" rx="1" fill="#fff"/><polygon points="13,10.5 17,7.5 17,13.5" fill="#fff"/></svg>
  </div>
</div>

<div class="field abs" style="top:486px">Regularmonthly investment...</div>
<div class="slider-label abs">length of investment</div>
<div class="slider-track abs"></div>
<div class="slider-fill abs"></div>
<div class="slider-thumb abs"></div>
<div class="range-tag abs" style="left:366px;width:34px">0 years</div>
<div class="range-tag abs" style="left:602px;width:40px">30 years</div>
<div class="field abs" style="top:583px">One time payout...</div>
<div class="or abs">or</div>
<div class="field abs" style="top:630px">Monthly payment...</div>
<div class="invest-btn abs">I WANT TO INVEST</div>

<svg class="abs" style="left:0;top:742px" width="702" height="315" viewBox="0 0 702 315">
  <polygon points="0,26 702,0 702,315 0,315" fill="var(--ice)"/>
  <polygon points="0,312 702,282 702,315 0,315" fill="var(--footer)"/>
</svg>

<div class="benefit-card abs" style="left:50px">
  <div class="benefit-art abs" role="img" aria-label="Illustration of a graduation cap on a stack of books" style="background:linear-gradient(180deg,#dff9fc 0%,#5a5a5a 30%,#e8553a 60%,#f5a623 100%)"></div>
  <div class="benefit-name abs">EDUCATION FOR KIDS</div>
</div>
<div class="benefit-card abs" style="left:255px">
  <div class="benefit-art abs" role="img" aria-label="Illustration of a retired golfer mid-swing" style="background:linear-gradient(180deg,#dff9fc 0%,#e8553a 45%,#45b9c6 80%,#dff9fc 100%)"></div>
  <div class="benefit-name abs">HAPPY LIFE AFTER<br>THEY RETIRE</div>
</div>
<div class="benefit-card abs" style="left:461px">
  <div class="benefit-art abs" role="img" aria-label="Illustration of a cuckoo clock with falling coins" style="background:linear-gradient(135deg,#e8553a 0%,#e8553a 50%,#f5a623 80%,#dff9fc 100%)"></div>
  <div class="benefit-name abs">REGULAR MONTHLY<br>PAYMENT</div>
</div>

<div class="abs" style="left:0;top:1056px;width:702px;height:122px;background:var(--footer)"></div>
<div class="footer-brand abs">PEROVALSTRINKA</div>
<div class="footer-rule abs"></div>
<nav class="footer-nav">
  <a style="left:206px">ABOUT US</a>
  <span class="footer-sep abs" style="left:264px">|</span>
  <a style="left:286px">FAQ</a>
  <span class="footer-sep abs" style="left:322px">|</span>
  <a style="left:345px">PRIVACY POLICY</a>
  <span class="footer-sep abs" style="left:427px">|</span>
  <a style="left:449px">CONTACT US</a>
</nav>
<div class="social abs" style="left:304px" aria-label="Social link"></div>
<div class="social abs" style="left:330px" aria-label="Social link"></div>
<div class="social abs" style="left:356px" aria-label="Social link"></div>
<div class="social abs" style="left:382px" aria-label="Social link"></div>
<div class="legal abs">perovalstrinka.com 2017. All rights reserved</div>

</body>
</html>
```